FernMieder - Werbebroschüre
Zielgruppe
FernMieder Arts & Crafts fertigt auf Maß Kostüme durch alle Jahrhunderte sowie Show und Bühnen-Kostüme: www.fern-mieder.de
Mit dem zu designenden Flyer sollen Institutionen und Firmen angesprochen werden, die 'noch nicht wissen', dass sie historische Bekleidung auf Maß benötigen: Museen (für die Führer/Personal), historische Eventlocations/Schlösser (um das Personal auch hochwertig aussehen zu lassen, oft kauft man hier im Faschingsbedarf), Veranstalter von Oldtimer-Rallys (historische Grid Girls).
Also, im Grunde muss ein Teil des Textes/der Botschaft neu werden, es soll kein Aklatsch der Homepage werden.
Flyer sollte nicht mehr als 4 Seiten haben, A5, Bruchfalz, Text und Style horizontal, die Bruchfalz also an der kützeren Seite.
Aufgabenstellung
Layout/Stil der Website, sehr plain, professionell, Vorelle-Style. Keine Schnörkel, kein Fasching, hochwertig,

```html
<!DOCTYPE html>
<html lang="en">
<head>
<meta charset="utf-8">
<title>FernMieder Arts &amp; Crafts – Brochure</title>
<link href="https://fonts.googleapis.com/css2?family=Jost:wght@300;400&display=swap" rel="stylesheet">
<style>
  :root {
    --stage: #b3b3b3;
    --ink: #0b0b0b;
    --paper: #ffffff;
    --text-light: #ffffff;
    --text-dark: #333333;
    --shadow: 0 2px 4px rgba(0,0,0,.35);
  }
  * { box-sizing: border-box; margin: 0; padding: 0; }
  html, body { width: 1030px; height: 1200px; overflow: hidden; background: var(--stage); }
  body {
    position: relative;
    font-family: 'Jost', sans-serif;
    font-weight: 300;
    -webkit-font-smoothing: antialiased;
    -moz-osx-font-smoothing: grayscale;
    text-rendering: geometricPrecision;
  }

  .sheet { position: absolute; height: 333px; overflow: hidden; box-shadow: var(--shadow); background: var(--ink); }
  .sheet--cover { left: 511px; top: 47px; width: 473px; }
  .sheet--inside { left: 40px; top: 430px; width: 946px; }
  .sheet--back { left: 39px; top: 813px; width: 473px; }

  .photo { position: absolute; }
  .brand { position: absolute; display: flex; flex-direction: column; align-items: center; color: var(--text-light); }
  .brand__circle { border: 2px solid var(--text-light); border-radius: 50%; }
  .brand__name { font-weight: 400; text-align: center; letter-spacing: .04em; line-height: 1.15; }

  /* cover */
  .cover__photo { left: 0; top: 0; width: 370px; height: 333px;
    background: linear-gradient(100deg, #4d5566 0%, #8a8468 22%, #c9bd94 45%, #a39570 62%, #3c3a33 82%, var(--ink) 100%); }
  .quote { position: absolute; right: 48px; top: 25px; text-align: right; color: var(--text-light); }
  .quote__text { font-size: 9.3px; font-weight: 300; }
  .quote__author { font-size: 5.5px; margin-top: 2px; }
  .cover .brand { left: 327px; top: 75px; width: 120px; }
  .cover .brand__circle { width: 104px; height: 104px; margin-bottom: 18px; }
  .cover .brand__name { font-size: 9px; }

  /* inside spread */
  .inside__portrait { left: 0; top: 0; width: 260px; height: 333px;
    background: linear-gradient(90deg, #a07a2a 0%, #c99a3a 18%, #3a2714 45%, #6b4a22 70%, #2a1b0d 88%, var(--ink) 100%); }
  .inside .brand { left: 303px; top: 46px; width: 80px; }
  .inside .brand__circle { width: 52px; height: 52px; margin-bottom: 10px; }
  .inside .brand__name { font-size: 5px; }
  .copy { position: absolute; font-size: 8.3px; line-height: 9.6px; text-align: justify; hyphens: auto; }
  .copy p + p { margin-top: 9.6px; }
  .copy--founded { left: 274px; top: 176px; width: 140px; color: var(--text-light); }
  .inside__white { position: absolute; left: 473px; top: 0; width: 473px; height: 333px; background: var(--paper); }
  .inside__group { left: 473px; top: 0; width: 244px; height: 183px;
    background: linear-gradient(135deg, #e2c3a8 0%, #cdae90 35%, #7c7a5a 65%, #a08a74 100%); }
  .inside__elder { left: 716px; top: 183px; width: 230px; height: 150px;
    background: radial-gradient(ellipse at 58% 40%, #8a5a36 0%, #5a4a2e 30%, #2e3a22 60%, #0e120c 100%); }
  .copy--materials { left: 766px; top: 50px; width: 131px; color: var(--text-dark); }
  .tagline { position: absolute; left: 571px; top: 237px; font-size: 10.4px; line-height: 12.3px; color: var(--text-dark); }

  /* back */
  .back__studio { left: 0; top: 0; width: 281px; height: 333px;
    background: linear-gradient(100deg, #5a5a5a 0%, #cfcfcf 28%, #9a9a9a 45%, #2a2a2a 65%, #151515 100%); }
  .back__strip { left: 434px; top: 0; width: 39px; height: 333px;
    background: linear-gradient(180deg, #e6e6e6 0%, #9c9c9c 40%, #4a4a4a 75%, #6a6a6a 100%); }
  .back .brand { left: 316px; top: 25px; width: 80px; }
  .back .brand__circle { width: 50px; height: 50px; margin-bottom: 12px; }
  .back .brand__name { font-size: 5px; }
  .back__copy { position: absolute; left: 301px; top: 145px; width: 125px; color: var(--text-light); font-size: 8px; line-height: 10.4px; }
  .back__copy p + p { margin-top: 10.4px; }
  .contact { margin-top: 9px; font-size: 8.3px; line-height: 12.8px; font-style: normal; }
  .contact__name { font-size: 9.2px; font-weight: 400; }
  .website { position: absolute; left: 84px; top: 302px; color: var(--text-light); font-size: 9.6px; font-weight: 400; letter-spacing: .12em; }
</style>
</head>
<body>

<section class="sheet sheet--cover cover" aria-label="Front cover">
  <div class="photo cover__photo" role="img" aria-label="Two women in Renaissance gowns with pearl jewellery, styled as an old portrait painting"></div>
  <blockquote class="quote">
    <p class="quote__text">»Fashion changes, but style endures«</p>
    <p class="quote__author">–Lise Vorelle</p>
  </blockquote>
  <div class="brand">
    <span class="brand__circle"></span>
    <span class="brand__name">FERNMIEDER<br>ARTS &amp; CRAFTS</span>
  </div>
</section>

<section class="sheet sheet--inside inside" aria-label="Inside spread">
  <div class="photo inside__portrait" role="img" aria-label="Man in a yellow Renaissance doublet with dark brocade jerkin"></div>
  <div class="brand">
    <span class="brand__circle"></span>
    <span class="brand__name">FERNMIEDER<br>ARTS &amp; CRAFTS</span>
  </div>
  <div class="copy copy--founded">
    <p>Founded in 2011 „FernMieder“ stands for exclusive bespoke authentic histo&shy;rical clothes through all ages as well a elaborate wedding, gothic and show dresses.</p>
    <p>Through our years of experience we are able to make garments to rise en détail again. Travel back in time to hear the rustle of silk and see the the luster of light in pearls &amp; gold buttons.</p>
  </div>
  <div class="inside__white"></div>
  <div class="photo inside__group" role="img" aria-label="Three people in 1940s and 1950s clothing, an officer's uniform in the middle, before a sandstone wall"></div>
  <div class="copy copy--materials">
    <p>We only process materials of hig&shy;hest quality and draw back on a long-standing network of speciali&shy;zed, often family-run, businesses.</p>
    <p>In our studio near Frankfurt/Main we welcome women and men of all sizes and create YOUR historic gar&shy;ment - whether for a fairytale wed&shy;ding, ball, theater, event, museum, reenactment or cosplay.</p>
  </div>
  <p class="tagline">We work with<br>genuine love<br>of tradition.</p>
  <div class="photo inside__elder" role="img" aria-label="Older man in a fur hat and fur-trimmed coat against a dark green backdrop"></div>
</section>

<section class="sheet sheet--back back" aria-label="Back cover">
  <div class="photo back__studio" role="img" aria-label="Black and white photo of the dressmaker beside a tailor's dummy in the studio"></div>
  <div class="photo back__strip" role="img" aria-label="Studio interior with dresses on forms, black and white"></div>
  <p class="website">www.fern-mieder.de</p>
  <div class="brand">
    <span class="brand__circle"></span>
    <span class="brand__name">FERNMIEDER<br>ARTS &amp; CRAFTS</span>
  </div>
  <div class="back__copy">
    <p>Need a historic costume for<br>a wedding, private occaison,<br>event, TV, show, drama or to<br>display in a museum or castle?</p>
    <p>We love to work for you<br>and your dream gown!</p>
    <p>Get in contact with us. Now!</p>
    <address class="contact">
      <span class="contact__name">FernMieder Arts &amp; Crafts</span><br>
      Dr. Helene Marburg<br>
      Lindenweg 12b<br>
      T: +49 17000 482915<br>
      E: info@fern-mieder.de
    </address>
  </div>
</section>

</body>
</html>
```